Bastion Guard Services

Our Company is a security business which needs a cut edge design, the final product should have all relevant information and maintain a bold but modern and professional look.

Target Market(s)

A cut edge design which will attract any audience

Industry/Entity Type

Security

Contact Information for Business Card

BASTION GUARD SERVICES

Daniel Kowalski
Operations Manager
Phone: 0419 357 216

Email: info@bastionguardex.com.au
Web: www.bastionguardex.com.au

Requirements
Must have
• Must be double sided and contain all relevant information and the company logo.

```html
<!DOCTYPE html>
<html lang="en">
<head>
<meta charset="UTF-8">
<title>Bastion Guard Services – Business Card</title>
<link rel="stylesheet" href="https://fonts.googleapis.com/css2?family=Roboto:ital,wght@0,400;0,700;1,300;1,400&display=swap">
<style>
  :root {
    --page-bg: #f4f4f4;
    --card-white: #ffffff;
    --ink-slate: #34454c;
    --accent-orange: #ec8a2f;
    --band-yellow: #f1b93b;
    --band-orange: #dd5f2b;
    --text-white: #ffffff;
  }
  * { margin: 0; padding: 0; box-sizing: border-box; }
  html, body {
    width: 1200px;
    height: 1098px;
    overflow: hidden;
    background: var(--page-bg);
    font-family: "Roboto", Arial, sans-serif;
  }
  .canvas {
    position: relative;
    width: 1200px;
    height: 1098px;
  }
  .card {
    position: absolute;
    left: 170px;
    width: 860px;
    height: 491px;
    overflow: hidden;
    box-shadow: 0 4px 14px rgba(0, 0, 0, 0.18);
  }
  .card-front { top: 40px; background: var(--card-white); }
  .card-back {
    top: 567px;
    background: linear-gradient(100deg, var(--band-yellow) 0%, var(--accent-orange) 55%, var(--band-orange) 100%);
  }

  .brand {
    position: absolute;
    right: 60px;
    top: 140px;
    width: 340px;
    display: flex;
    flex-direction: column;
    align-items: center;
    gap: 18px;
  }
  .brand-mark {
    width: 22px;
    height: 22px;
    background: var(--accent-orange);
  }
  .brand-name {
    font-weight: 700;
    font-size: 36px;
    line-height: 1.15;
    letter-spacing: 1px;
    color: var(--ink-slate);
    text-align: center;
  }

  .contact {
    position: absolute;
    left: 75px;
    top: 322px;
    font-size: 29px;
    line-height: 37px;
    color: var(--ink-slate);
  }
  .contact-name { font-weight: 400; }
  .contact-role { font-style: italic; font-weight: 300; color: var(--accent-orange); }
  .contact-label { font-weight: 400; }
  .contact-value { font-weight: 300; color: var(--accent-orange); }

  .web-band {
    position: absolute;
    left: 0;
    bottom: 0;
    width: 100%;
    height: 58px;
    background: linear-gradient(90deg, var(--band-yellow) 0%, var(--accent-orange) 50%, var(--band-orange) 100%);
    display: flex;
    align-items: center;
  }
  .web-address {
    margin-left: 160px;
    font-style: italic;
    font-weight: 300;
    font-size: 32px;
    letter-spacing: 0.5px;
    color: var(--text-white);
  }
</style>
</head>
<body>
<main class="canvas">
  <section class="card card-front" aria-label="Business card front">
    <div class="brand">
      <span class="brand-mark" aria-hidden="true"></span>
      <div class="brand-name">BASTION GUARD SERVICES</div>
    </div>

    <div class="contact">
      <p><span class="contact-name">Daniel Kowalski</span> <span class="contact-role">Operations Manager</span></p>
      <p><span class="contact-label">P:</span> <span class="contact-value">0419 357 216</span></p>
      <p><span class="contact-label">E:</span> <span class="contact-value">info@bastionguardex.com.au</span></p>
    </div>

    <div class="web-band">
      <span class="web-address">www.bastionguardex.com.au</span>
    </div>
  </section>

  <section class="card card-back" aria-label="Business card back"></section>
</main>
</body>
</html>
```